High-end Management Consulting Website

I am looking for a design that feels very high end and professional and very serious feeling. I would like a site that uses a lot of white space, with colors in the blue, grey family. You can use a very small about of the orange and green in the logo, but it needs to be a very small amount.

I like images similar to a rock climber helping another one up a mountain. I would love other imagery throughout the site of mountain ranges and people making it to the top.

When you think of the feel imagine people in suites, very corporate feeling. Very much focused on helping company leadership and CEOs solve problems.

From a functionality standpoint https://ninebramwell.com has a good deal of similar content- However, I do not like the colors or the design. I like graphics on websites similar to https://www.harrowcapitalgroup.com.

I like clean with lots of white space.

The link below has all of the content and design comments. https://files.quillnet.com/doc/7QpLm3XzR8vTt2KwYh5NbD9sFgJc4EuA6oViWr0Ue/view?share=open

Target Market(s)

High end businesses and very experienced executives.

Industry/Entity Type

Consulting

Coding

Coded - Design and coding required

Number of Pages Required

5+ page

Font styles to use
Sans Serif

Colors

Designer to choose colors to be used in the design.

Requirements
Must have
• white space, blues some gray, clean feel VERY LITTLE use of accent colors.

I want to have a centered navigation bar.
I would like to have a secondary scrolling image.
Nice to have
• High end imagery that speaks to what is being said in the site.
This is not the main image I want to see but I like imagery like this for the main home page.
https://www.pixelmarrow.com/image-photo/couple-hiking-help-each-other-silhouette-731864205
Should not have
• Please do not use dated images or blocky feeling. Please also do not go overboard using the icon in the design.

```html
<!DOCTYPE html>
<html lang="en">
<head>
<meta charset="utf-8">
<title>Keystone Ridge Partners</title>
<link rel="stylesheet" href="https://fonts.googleapis.com/css2?family=Open+Sans:wght@400;600&display=swap">
<style>
  :root {
    --topbar-bg: #e9f3fa;
    --nav-bg: #f7f8f9;
    --ink: #3d4a55;
    --ink-dark: #1e3a57;
    --link-blue: #3a9ad9;
    --social-blue: #2b93d8;
    --accent-green: #8dc63f;
    --hero-deep: #0a2a5c;
    --hero-mid: #0e4a7a;
    --hero-teal: #1b6a6a;
    --white: #ffffff;
  }
  * { margin: 0; padding: 0; box-sizing: border-box; }
  html, body { width: 1200px; height: 525px; overflow: hidden; }
  body { font-family: "Open Sans", Arial, sans-serif; color: var(--ink); background: var(--white); position: relative; }

  .topbar { position: absolute; left: 0; top: 0; width: 1200px; height: 30px; background: var(--topbar-bg); }
  .social-links { position: absolute; left: 87px; top: 6px; display: flex; gap: 8px; }
  .social-dot { width: 18px; height: 18px; border-radius: 50%; background: var(--social-blue); }
  .topbar-note { position: absolute; right: 87px; top: 8px; font-size: 10px; line-height: 13px; color: var(--ink); white-space: nowrap; }
  .topbar-note em { color: var(--link-blue); }

  .site-nav { position: absolute; left: 0; top: 30px; width: 1200px; height: 67.5px; background: var(--nav-bg); }
  .brand { position: absolute; left: 87px; top: 16px; display: flex; align-items: center; gap: 7px; }
  .brand-mark { width: 14px; height: 14px; background: var(--ink-dark); }
  .brand-name { font-size: 11px; font-weight: 600; line-height: 14px; color: var(--ink-dark); letter-spacing: 0.3px; width: 110px; }
  .nav-item { position: absolute; top: 25px; font-size: 12px; line-height: 17px; color: var(--ink); text-decoration: none; white-space: nowrap; }
  .nav-item.is-active { color: var(--link-blue); }
  .nav-item.is-active::after { content: ""; position: absolute; left: 0; right: 0; top: 40px; height: 2px; background: var(--link-blue); }
  .btn-outline { position: absolute; left: 911px; top: 17px; width: 202px; height: 34px; border: 1.5px solid var(--accent-green); border-radius: 3px; color: var(--accent-green); font-size: 10.5px; display: flex; align-items: center; justify-content: center; text-transform: uppercase; white-space: nowrap; }

  .hero { position: absolute; left: 0; top: 97.5px; width: 1200px; height: 427.5px; overflow: hidden; }
  .hero-photo { position: absolute; inset: 0;
    background: linear-gradient(180deg, var(--hero-mid) 0%, var(--hero-teal) 45%, #0d3a66 68%, var(--hero-deep) 100%); }
  .hero-title { position: absolute; left: 0; width: 1200px; top: 86px; text-align: center; color: var(--white); font-size: 26px; font-weight: 600; line-height: 43.5px; }
  .hero-copy { position: absolute; left: 0; width: 1200px; top: 180px; text-align: center; color: var(--white); font-size: 13.5px; line-height: 22.5px; }
  .btn-solid { position: absolute; left: 499px; top: 267px; width: 202px; height: 34px; border-radius: 3px; background: var(--accent-green); color: var(--white); font-size: 10.5px; display: flex; align-items: center; justify-content: center; text-transform: uppercase; white-space: nowrap; }
  .slider-dots { position: absolute; left: 587px; top: 406px; display: flex; gap: 4.5px; }
  .slider-dot { width: 5.5px; height: 5.5px; border-radius: 50%; border: 1px solid var(--white); }
  .slider-dot.is-current { background: var(--white); }
</style>
</head>
<body>
  <header class="topbar">
    <div class="social-links" aria-label="Social links">
      <span class="social-dot"></span><span class="social-dot"></span><span class="social-dot"></span><span class="social-dot"></span>
    </div>
    <p class="topbar-note"><em>Learn how</em> companies are at keystone advantage during COVID-19 Pandemic</p>
  </header>

  <nav class="site-nav">
    <div class="brand"><span class="brand-mark"></span><span class="brand-name">KEYSTONE RIDGE PARTNERS</span></div>
    <a class="nav-item is-active" style="left:309px">Home</a>
    <a class="nav-item" style="left:427px">Advisory services</a>
    <a class="nav-item" style="left:607px">About us</a>
    <a class="nav-item" style="left:741px">Work with us</a>
    <a class="btn-outline">Schedule an appointment</a>
  </nav>

  <section class="hero">
    <div class="hero-photo" role="img" aria-label="Night city skyline over a river, tinted in deep blue and green"></div>
    <h1 class="hero-title">From start-ups to global corporations, we bring knowledge, expertise<br>and powerful networks creating impactful business outcomes.</h1>
    <p class="hero-copy">Our partners have served in executive leadership for fortune 1000 global organizations, served at the highest levels<br>of office and managed billions in buy and sell side transactions. Our experience, founding, scaling, exiting and<br>acquiring companies along the way, gives our team a unique understanding of the clients we serve.</p>
    <a class="btn-solid">Schedule an appointment</a>
    <div class="slider-dots"><span class="slider-dot is-current"></span><span class="slider-dot"></span><span class="slider-dot"></span></div>
  </section>
</body>
</html>
```